Packaging Design for Boneless Picnic Ham

We are Tidewell Provisions Limited, a company based in Trinidad which is located within the Caribbean. We produce and sell a plethora of meat products including a variety of hams, sausages and even bacon.

We require a packaging design for a ham product. This product is packaged within a cryovac (11" X 18") shrink bag which would be used to package our Boneless Picnic Ham which weighs 2.5 Kilograms.

The design space should be 7 inches wide and 6 inches in height. The design is 3 inches from the bottom and 2 inches off each side.

Our target audience comprises of caterers as well as the average household folk. What sets our product apart is that it is has a great taste, 20% less salt and is affordable and easy. We commonly refer to it as the "Sunday Roast Joint".

Attached below, is our logo which you must incorporate onto the design. We also request that the header be "Hickory Smoked Boneless Picnic Ham".

Target Market(s)

Caterers and Average Household Folk

Font styles to use
Sans Serif

Requirements
Must have
• The Tidewell Provisions Company Logo and the header must have "Hickory Smoked Boneless Picnic Ham"
Nice to have
• Maximum Creativity
Should not have
• No animal artwork should be included onto the design

```html
<!DOCTYPE html>
<html lang="en">
<head>
<meta charset="utf-8">
<title>Tidewell Provisions – Hickory Smoked Boneless Picnic Ham</title>
<link href="https://fonts.googleapis.com/css2?family=Oswald:wght@600&family=Open+Sans:wdth,wght@75..100,400..800&display=swap" rel="stylesheet">
<style>
  :root {
    --page-bg: #ececec;
    --frame-red: #e21f3b;
    --sky: #edf1f8;
    --sun: #fdd017;
    --navy: #2c3a93;
    --ink: #1d1d24;
    --panel: #ffffff;
  }
  * { margin: 0; padding: 0; box-sizing: border-box; }
  html, body {
    width: 1200px; height: 1000px; overflow: hidden;
    background: var(--page-bg);
    font-family: "Open Sans", Arial, sans-serif;
  }
  .label {
    position: absolute; left: 70px; top: 45px;
    width: 1062px; height: 910px;
    border: 10px solid var(--frame-red);
    border-radius: 22px;
    background: var(--sun);
    overflow: hidden;
  }
  .label__header {
    position: absolute; left: 0; top: 0; width: 100%; height: 242px;
    background: var(--sky);
    display: flex; align-items: center; justify-content: center; gap: 16px;
  }
  .brand-dot { width: 34px; height: 34px; border-radius: 50%; background: var(--navy); }
  .brand-name {
    font-weight: 800; font-size: 46px; color: var(--navy); letter-spacing: -0.5px;
  }
  .title {
    position: absolute; left: 50%;
    font-family: "Oswald", "Arial Narrow", sans-serif; font-weight: 600;
    text-transform: uppercase; line-height: 1; white-space: nowrap;
    transform-origin: center center;
  }
  .title--accent {
    top: 272px; font-size: 120px; color: var(--frame-red); letter-spacing: -1px;
    transform: translateX(-50%) scaleX(0.945);
  }
  .title--main {
    top: 407px; font-size: 122px; color: var(--navy); letter-spacing: -1.5px;
    transform: translateX(-50%) scaleX(0.93);
  }
  .copy {
    position: absolute; left: 21px; width: 598px;
    font-size: 11.6px; line-height: 14px; color: var(--ink);
    text-align: justify; overflow: hidden;
  }
  .copy--intro { top: 557px; height: 84px; }
  .copy--detail { top: 642px; height: 156px; }
  .copy--note { top: 800px; width: 432px; height: 62px; font-size: 12.6px; line-height: 14.5px; }
  .weight {
    position: absolute; left: 475px; top: 772px;
    font-size: 70px; font-weight: 400; font-stretch: 80%;
    color: var(--navy); letter-spacing: -1px; line-height: 1.35;
  }
  .nutrition {
    position: absolute; left: 645px; top: 557px; width: 368px; height: 175px;
    background: var(--panel); padding: 6px 8px;
    display: flex; gap: 10px; color: #333;
  }
  .nutrition__lead { width: 160px; }
  .nutrition__title { font-weight: 800; font-size: 24px; line-height: 30px; color: #222; }
  .nutrition__meta { font-size: 9px; line-height: 11px; margin-top: 4px; }
  .nutrition__meta strong { font-weight: 800; }
  .nutrition__foot { font-size: 7px; line-height: 9px; margin-top: 2px; }
  .nutrition__table { flex: 1; font-size: 9px; }
  .nutrition__row {
    display: flex; justify-content: space-between;
    border-bottom: 1px solid #555; padding: 3px 0; line-height: 12px;
  }
  .nutrition__row--head { font-size: 7px; border-bottom: 4px solid #222; padding: 0 0 2px; }
  .nutrition__row--thick { border-bottom: 4px solid #222; }
  .nutrition__row strong { font-weight: 800; }
  .nutrition__row--indent { padding-left: 14px; }
  .nutrition__small { font-size: 7px; line-height: 9px; margin-top: 3px; }
  .claim {
    position: absolute; right: 22px; font-weight: 800;
    font-size: 45px; line-height: 1; letter-spacing: 0.3px; text-transform: uppercase;
    white-space: nowrap;
  }
  .claim--serve { top: 755px; color: var(--navy); }
  .claim--salt { top: 811px; color: var(--frame-red); }
</style>
</head>
<body>
<main class="label">
  <header class="label__header">
    <span class="brand-dot"></span>
    <span class="brand-name">Tidewell Provisions</span>
  </header>

  <h1 class="title title--accent">Hickory Smoked</h1>
  <h2 class="title title--main">Boneless Picnic Ham</h2>

  <p class="copy copy--intro">Lorem ipsum dolor sit amet, consectetur adipisicing elit, sed do eiusmod tempor incididunt ut labore et dolore magna aliqua. Ut enim ad minim veniam, quis nostrud exercitation. Lorem ipsum dolor sit amet, consectetur adipisicing elit, sed do eiusmod tempor incididunt ut labore et dolore magna aliqua. Ut enim ad minim veniam, quis nostrud exercitation. Lorem ipsum dolor sit amet, consectetur adipisicing elit, sed do eiusmod tempor incididunt ut labore et dolore magna aliqua. Ut enim ad minim veniam, quis nostrud exercitation.</p>

  <p class="copy copy--detail">Lorem ipsum dolor sit amet, consectetur adipisicing elit, sed do eiusmod tempor incididunt ut labore et dolore magna aliqua. Ut enim ad minim veniam, quis nostrud exercitation. Lorem ipsum dolor sit amet, consectetur adipisicing elit, sed do eiusmod tempor incididunt ut labore et dolore magna aliqua. Ut enim ad minim veniam, quis nostrud exercitation. Lorem ipsum dolor sit amet, consectetur adipisicing elit, sed do eiusmod tempor incididunt ut labore et dolore magna aliqua. Ut enim ad minim veniam, quis nostrud exercitation. Lorem ipsum dolor sit amet, consectetur adipisicing elit, sed do eiusmod tempor incididunt ut labore et dolore magna aliqua. Ut enim ad minim veniam, quis nostrud exercitation. Lorem ipsum dolor sit amet, consectetur adipisicing elit, sed do eiusmod tempor incididunt ut labore et dolore magna aliqua. Ut enim ad minim veniam, quis nostrud exercitation. Lorem ipsum dolor sit amet, consectetur adipisicing elit, sed do eiusmod tempor incididunt ut labore et dolore magna aliqua. Ut enim ad minim veniam, quis nostrud exercitation.</p>

  <p class="copy copy--note">Lorem ipsum dolor sit amet, consectetur adipisicing elit, sed do eiusmod tempor incididunt ut labore et dolore magna aliqua. Ut enim ad minim veniam, quis nostrud exercitation. Lorem ipsum dolor sit amet, consectetur adipisicing elit.</p>

  <div class="weight">700 g</div>

  <section class="nutrition" aria-label="Nutrition facts">
    <div class="nutrition__lead">
      <div class="nutrition__title">Nutrition<br>Facts</div>
      <div class="nutrition__meta">Serving Size 2 slices (56g)<br>Servings Per Container 12<br><strong>Calories</strong> 70</div>
      <div class="nutrition__foot">*Percent Daily Values are based on a 2,000 calorie diet.</div>
    </div>
    <div class="nutrition__table">
      <div class="nutrition__row nutrition__row--head"><span>Amount / Serving</span><span>% Daily Value</span></div>
      <div class="nutrition__row"><span><strong>Total Fat</strong> 2g</span><span>3%</span></div>
      <div class="nutrition__row"><span><strong>Sodium</strong> 480mg</span><span>20%</span></div>
      <div class="nutrition__row"><span><strong>Total Carbohydrate</strong> 1g</span><span>0%</span></div>
      <div class="nutrition__row nutrition__row--indent"><span>Sugars 1g</span><span></span></div>
      <div class="nutrition__row nutrition__row--thick"><span><strong>Protein</strong> 11g</span><span></span></div>
      <div class="nutrition__row"><span>Vitamin C 2%</span><span></span></div>
      <div class="nutrition__small">Not a significant source of dietary fiber, vitamin A, calcium and iron.</div>
    </div>
  </section>

  <div class="claim claim--serve">Ready to Serve</div>
  <div class="claim claim--salt">20% Less Salt</div>
</main>
</body>
</html>
```